Business Card Design Project - Tall Maple

We are looking for a new business card design. Our company name is Tall Maple Communication Solutions. Our primary function is to provide our clients with communication solutions. These solutions include commercial phone systems and T1 and Fiber Internet lines. Another major part of the business is cabling new buildings with CAT5 cable for both data and phone.

Industry/Entity Type

Communication

Requirements
Must have
• The cards need to be two sided and have some bleeding edge color.
Nice to have
• We are going to upload our current logo BUT we are not married to this logo. If you want to incorporate a re-designed logo with the new business card - please feel free to do so. We are looking for a new bold look that is very colorful yet professional.

```html
<!DOCTYPE html>
<html lang="en">
<head>
<meta charset="utf-8">
<title>Tall Maple Communication Solutions – Business Card</title>
<link rel="stylesheet" href="https://fonts.googleapis.com/css2?family=Mulish:wght@400;800&display=swap">
<style>
  :root {
    --backdrop: #a3a3a3;
    --card: #ffffff;
    --stripe-light: #fbfbfb;
    --stripe-dark: #eeeeee;
    --band: #9db8f2;
    --mark: #0b1a3c;
    --ink: #555555;
    --ink-strong: #3f3f3f;
  }
  * { box-sizing: border-box; margin: 0; padding: 0; }
  html, body {
    width: 1200px; height: 1200px; overflow: hidden;
    background: var(--backdrop);
    font-family: "Mulish", sans-serif;
  }
  .card {
    position: absolute; left: 206px; width: 760px; height: 452px;
    background: var(--card); overflow: hidden;
  }
  .card--front { top: 89px; }
  .card--back { top: 616px; }
  .card__texture {
    position: absolute; inset: 0;
    background: linear-gradient(135deg, var(--stripe-light), var(--stripe-dark));
  }
  .brand-band {
    position: absolute; left: 0; top: 37px; width: 100%; height: 190px;
    background: var(--band);
  }
  .band-shade {
    position: absolute; left: 0; top: 227px; width: 100%; height: 95px;
    background: linear-gradient(to bottom, rgba(110,110,110,0.55), rgba(160,160,160,0) );
  }
  .brand-mark {
    position: absolute; left: 102px; top: 38px;
    width: 188px; height: 188px; border-radius: 50%;
    background: var(--mark);
  }
  .brand-name {
    position: absolute; left: 310px; top: 76px;
    font-weight: 800; font-size: 30px; letter-spacing: 0.5px;
    color: var(--mark); text-transform: uppercase;
  }
  .brand-tagline {
    position: absolute; left: 336px; top: 114px;
    font-weight: 400; font-size: 15px; letter-spacing: 1px;
    color: var(--mark); text-transform: uppercase;
  }
  .contact {
    position: absolute; left: 154px; top: 284px;
    color: var(--ink); font-size: 20px; line-height: 37px;
  }
  .contact__name { font-weight: 800; color: var(--ink-strong); }
  .numbers {
    position: absolute; left: 0; top: 110px; width: 100%;
    text-align: center; color: var(--ink);
    font-size: 34px; line-height: 62px; list-style: none;
  }
  .numbers__label { font-weight: 800; }
</style>
</head>
<body>
  <section class="card card--front">
    <div class="card__texture" role="img" aria-label="Light grey diagonal stripe texture"></div>
    <div class="brand-band"></div>
    <div class="band-shade"></div>
    <div class="brand-mark"></div>
    <div class="brand-name">Tall Maple</div>
    <div class="brand-tagline">Communication Solutions</div>
    <address class="contact">
      <div class="contact__name">Marcus Ellery</div>
      <div>4810 N Ridgeview Avenue, Suite 300</div>
      <div>Tempe, AZ 85281</div>
    </address>
  </section>

  <section class="card card--back">
    <div class="card__texture" role="img" aria-label="Light grey diagonal stripe texture"></div>
    <ul class="numbers">
      <li><span class="numbers__label">Office:</span> 555.214.3308</li>
      <li><span class="numbers__label">Cell:</span> 555.867.1942</li>
      <li><span class="numbers__label">24/7:</span> 800.555.0147</li>
      <li><span class="numbers__label">Fax:</span> 800.555.0193</li>
    </ul>
  </section>
</body>
</html>
```